Tailmart.com Dog Coupon Site Website Design

FurSaver - Dog Coupon Site Design Brief

Project Overview
**Site Name:** TailMart.com
**Purpose:** A modern coupon aggregation platform specifically for dog and pet-related products and services
**Target Audience:** Dog owners, pet enthusiasts, budget-conscious pet parents

Brand Identity & Visual Direction

Typography
- **Headers:** Modern sans-serif (Inter or similar) - Clean and friendly
- **Body:** Readable sans-serif with good mobile legibility
- **Accent:** Playful but professional font for coupon codes

Design Principles
- **Flat Design:** Clean, minimal with subtle shadows
- **Friendly & Approachable:** Rounded corners, soft edges
- **Trust-Building:** Clear pricing, transparent savings
- **Scannable:** Easy-to-read coupon codes and offers

## User Experience & Functionality

### Homepage Features
1. **Hero Section**
- Clear value proposition
- Search functionality
- Featured savings highlight

2. **Coupon Cards**
- One-click copy functionality
- Clear discount display
- Store/brand logos
- Expiration dates
- "Get Deal" call-to-action

3. **Navigation**
- Categories (Food, Toys, Health, Services, etc.)
- Popular stores
- Latest deals

### Interactive Elements
- **Copy Button:** Instant feedback when coupon copied
- **Deal Pages:** Detailed offer information, terms, store details
- **Search & Filter:** By category, store, discount amount
- **Mobile Menu:** Hamburger navigation for mobile

## Technical Requirements

### Responsive Design
- **Mobile-First:** Optimized for touch interactions
- **Tablet:** Adapted layout for medium screens
- **Desktop:** Full-width utilization with sidebar potential

### Performance
- **Fast Loading:** Optimized images, minimal JavaScript
- **Accessibility:** WCAG compliant, screen reader friendly
- **SEO Optimized:** Structured data for deals and offers

## Content Strategy

### Deal Categories
- Dog Food & Treats
- Toys & Accessories
- Health & Grooming
- Training & Services
- Outdoor & Travel

### Key Messaging
- "Save on everything your dog loves"
- "Verified deals updated daily"
- "Your pup deserves the best for less"

## Conversion Optimization

### Trust Elements
- Deal verification badges
- User reviews/ratings
- Clear savings calculations
- Expiration date transparency

### Call-to-Actions
- "Copy Code" (primary action)
- "Get Deal" (secondary action)
- "View All [Store] Deals"

## Success Metrics
- Coupon copy rate
- Click-through to retailer
- User return visits
- Mobile vs desktop usage
- Category performance

This design brief ensures a user-friendly, trustworthy platform that makes finding and using pet deals effortless while maintaining a warm, dog-loving community feel.

1. Design Objective
Create a warm, energetic space where dog lovers instantly feel welcomed and confident they’re finding genuine savings for their furry friends. Everything from the layout to the smallest icon should reinforce trust, delight, and simplicity.
2. Visual Personality
Color Palette: Soft, cheerful hues—think warm yellows and gentle blues—that evoke sunshine and playfulness without overwhelming.
Typography:
Headings: A modern, friendly sans‑serif (like Inter) with open letterforms to feel approachable.
Body Copy: Highly legible sans‑serif with generous line spacing for comfort on small screens.
Accent Font: A slightly quirky, hand‑drawn style used sparingly for coupon codes and special call‑outs, giving a personal, “paw‑picked” touch.
Imagery & Icons: Real‑life photographs of happy dogs interspersed with clean line‑icons of bones, paw prints, and hearts. Rounded shapes and subtle shadows keep the look soft and contemporary.
3. Layout & Hierarchy
Hero Area:
Full‑bleed image of a joyful dog, overlaid with a single, punchy tagline (“Save on everything your dog loves”).
Prominent search bar centered to invite exploration.
Offer Grid:
Generous white space around each coupon card so the eye can rest and scan easily.
Coupon cards feature a bold discount label, brand logo, and a friendly “Get Deal” button.
A playful “Copied!” animation briefly replaces the button once the code is grabbed.
Navigation:
A fixed header with clear category labels (Food, Toys, Health, Services).
A secondary “Popular Stores” carousel below to spotlight key partners.
4. Interaction & Motion
Micro‑interactions:
Hover state for cards subtly lifts the card and deepens its shadow, inviting a click.
Copy‑code button pulses once on hover, hinting at its one‑click magic.
Transitions:
Smooth fades between deal filters and search results to reassure users that the site is responding.
Loading indicators shaped like spinning collars or wagging tails to keep the theme consistent.
5. Accessibility & Inclusivity
Ensure all text meets contrast standards so every pet parent—regardless of vision—can read offers with ease.
Interactive elements sized for easy tapping on touchscreens.
Alt‑text for all imagery describing dogs, products, and actions for screen‑reader users.
6. Emotional Tone
From the moment someone lands on TailMart.com, they should feel the joy of treating their dog without guilt. Friendly copy (“Your pup deserves the best for less”) paired with bright visuals will create a sense of community and shared passion.
7. Success by Design
Scan‑ability: Users should spot great deals in under two seconds.
Trust Signals: Badges (“Verified Savings”), clear expiration dates, and reviewer star icons should feel earned and prominent.
Return Visits: A “My Favorite Deals” heart icon encourages saving and returning, reinforced by subtle reminders in the UI.
This design approach keeps dog lovers front and center—making sure every graphic, font choice, and interaction feels like it was lovingly tailored for them.

Target Market(s)

Dog Lovers looking for good deals

Industry/Entity Type

Coupon Code

Number of Pages Required

4 page

Font styles to use
Sans Serif

Requirements
Must have
• Modern look, coupon copy cards it's a deal site and I want the coupon code and copy in the coupon card, blog section, review section, modern footer/header
Nice to have
• Modern coupon code website, easy to use

```html
<!DOCTYPE html>
<html lang="en">
<head>
<meta charset="utf-8">
<title>TailMart.com – Save on everything your dog loves</title>
<link rel="stylesheet" href="https://fonts.googleapis.com/css2?family=Inter:wght@400;500;600;700;800&display=swap">
<style>
:root{
  --orange:#f7931e;
  --orange-deep:#ee7f10;
  --teal:#128b88;
  --teal-dark:#0c4f4c;
  --ink:#1b1b1b;
  --muted:#6d6d6d;
  --line:#e7e7e7;
  --soft:#f2f2f3;
  --soft-2:#f6f6f7;
  --footer:#131313;
  --white:#ffffff;
}
*{box-sizing:border-box;margin:0;padding:0}
html,body{width:1200px;height:4491px;overflow:hidden}
body{position:relative;font-family:"Inter",sans-serif;color:var(--ink);background:var(--white)}

/* Header */
.site-header{position:absolute;left:0;top:0;width:1200px;height:88px;background:var(--white);z-index:3}
.brand{position:absolute;display:flex;align-items:center;gap:10px;font-weight:800;font-size:32px;color:var(--orange);letter-spacing:-.5px}
.brand__mark{width:36px;height:44px;border-radius:8px;background:var(--orange)}
.site-header .brand{left:153px;top:22px}
.nav{position:absolute;top:34px;left:445px;font-size:15px}
.nav a{color:var(--ink);text-decoration:none;position:absolute;white-space:nowrap}
.nav a.is-active{color:var(--orange);text-decoration:underline;text-underline-offset:4px}
.socials{position:absolute;display:flex;gap:6px}
.socials span{width:26px;height:26px;border-radius:50%;background:var(--ink);display:block}
.site-header .socials{left:910px;top:31px}

/* Hero */
.hero{position:absolute;left:0;top:88px;width:1200px;height:386px;
  background:radial-gradient(ellipse 260px 300px at 940px 190px,#f3efe8 0%,#e6ddcf 40%,rgba(230,221,207,0) 70%),
  linear-gradient(180deg,#56763a 0%,#6f9b3f 45%,#9cc04c 75%,#7ea53a 100%)}
.hero__title{position:absolute;left:150px;top:50px;font-size:58px;line-height:68px;font-weight:800;color:var(--white);letter-spacing:-1px}
.search{position:absolute;left:150px;top:283px;width:600px;height:49px;background:var(--white);border-radius:25px;display:flex;align-items:center}
.search__select{width:155px;padding-left:22px;font-size:13px;display:flex;justify-content:space-between;align-items:center;padding-right:18px;border-right:1px solid #ddd;height:30px}
.search__input{padding-left:22px;font-size:13px;color:#9a9a9a;font-style:italic;flex:1}
.search__btn{width:34px;height:34px;border-radius:50%;background:var(--orange);margin-right:8px;display:flex;align-items:center;justify-content:center}

.deco{position:absolute;border-radius:50%}

/* Section titles */
.section-title{position:absolute;left:0;width:1200px;text-align:center;font-size:38px;font-weight:800;letter-spacing:-.5px}
.section-title::after{content:"";display:block;width:40px;height:2px;background:var(--ink);margin:22px auto 0}

/* Coupon cards */
.grid4{position:absolute;left:150px;width:900px;display:grid;grid-template-columns:repeat(4,211px);column-gap:18.6px}
.coupon{position:relative;height:494px;background:var(--white);border-radius:8px;box-shadow:0 2px 12px rgba(0,0,0,.08)}
.coupon.is-lifted{transform:translateY(-14px);box-shadow:0 8px 22px rgba(0,0,0,.16)}
.coupon__media{height:174px;border-radius:8px 8px 0 0;position:relative}
.badge-off{position:absolute;top:16px;left:10px;background:var(--orange);color:var(--white);font-size:11px;font-weight:700;padding:4px 9px;border-radius:12px}
.tag{position:absolute;left:24px;top:165px;background:var(--white);border:1px solid var(--teal);color:var(--teal);font-size:10px;padding:2px 10px;border-radius:10px}
.store-name{position:absolute;left:24px;top:205px;font-size:24px;font-weight:800;color:var(--orange);letter-spacing:-.5px}
.desc{position:absolute;left:24px;top:262px;width:165px;font-size:14px;line-height:20px}
.price{position:absolute;left:24px;top:318px;font-size:17px;font-weight:700}
.price s{font-size:12px;color:#999;font-weight:400;margin-left:4px}
.expiry{position:absolute;left:24px;top:357px;font-size:12px;color:#333}
.divider{position:absolute;left:12px;right:12px;top:392px;border-top:1px dashed var(--line)}
.btn{position:absolute;left:25px;width:161px;height:26px;border-radius:6px;font-size:12px;font-weight:500;color:var(--white);display:flex;align-items:center;justify-content:center}
.btn--copy{top:419px;background:var(--teal)}
.btn--copied{background:var(--teal-dark)}
.btn--deal{top:457px;height:30px;background:var(--orange);font-weight:700}
.upto{position:absolute;left:24px;top:316px;display:flex;align-items:center;gap:8px;font-size:18px;font-weight:700}
.upto span{background:var(--ink);color:var(--white);font-size:11px;padding:2px 6px;border-radius:8px}

.btn-outline{position:absolute;width:155px;height:47px;border:1.5px solid var(--orange);border-radius:8px;color:var(--orange);font-weight:700;font-size:14px;display:flex;align-items:center;justify-content:center;background:var(--white)}

/* Categories */
.cat-band{position:absolute;left:0;top:1875px;width:1200px;height:562px;background:var(--soft)}
.cat-card{position:absolute;top:2034px;width:289px;height:296px;border-radius:6px;overflow:hidden}
.cat-card__label{position:absolute;left:0;right:0;bottom:0;height:60px;display:flex;justify-content:space-between;align-items:center;padding:10px 20px 0;color:var(--white);font-size:22px;background:linear-gradient(180deg,rgba(0,0,0,0),rgba(0,0,0,.45))}
.dots{position:absolute;left:0;width:1200px;display:flex;justify-content:center;gap:12px}
.dots i{width:12px;height:12px;border-radius:50%;background:#2b2b2b;display:block}
.dots i.on{background:var(--orange)}

.arrow-btn{position:absolute;width:44px;height:44px;border-radius:50%;border:1.5px solid #8a8a8a;display:flex;align-items:center;justify-content:center;background:var(--white)}

/* Stores */
.stores-band{position:absolute;left:0;top:3153px;width:1200px;height:501px;background:var(--soft-2)}
.store-grid{position:absolute;left:152px;top:3314px;width:898px;display:grid;grid-template-columns:repeat(5,168px);column-gap:14.5px;row-gap:24px}
.store-tile{height:86px;background:var(--white);border-radius:8px;box-shadow:0 2px 8px rgba(0,0,0,.06);display:flex;align-items:center;justify-content:center;gap:8px;font-size:15px;font-weight:700;color:#333}
.store-tile i{width:22px;height:22px;border-radius:50%;background:#333;display:block}

/* Reviews */
.reviews-title{position:absolute;left:148px;top:3700px;font-size:38px;font-weight:800;letter-spacing:-.5px}
.reviews-title::after{content:"";display:block;width:40px;height:2px;background:var(--ink);margin-top:22px}
.rating{position:absolute;left:810px;top:3720px;display:flex;align-items:center;gap:14px}
.rating__badge{width:42px;height:42px;border-radius:50%;background:var(--teal)}
.rating__text{font-size:12px;color:#333;margin-top:6px}
.stars{display:flex;gap:3px}
.review{position:absolute;top:3814px;width:288px;height:276px;border:1px solid #cfcfcf;border-radius:8px;padding:22px 40px 0 40px}
.review__quote{font-size:48px;font-weight:800;color:var(--orange);line-height:30px;height:30px}
.review .stars{margin-top:12px}
.review__text{font-size:12.5px;line-height:18px;color:#333;margin-top:12px}
.reviewer{display:flex;align-items:center;gap:14px;margin-top:16px;font-size:11px;color:#444;line-height:17px}
.reviewer i{width:38px;height:38px;border-radius:50%;background:#c9b4a0;display:block}

/* Footer */
.site-footer{position:absolute;left:0;top:4200px;width:1200px;height:291px;background:var(--footer);color:var(--white)}
.site-footer .brand{left:150px;top:80px;color:var(--orange)}
.f-col{position:absolute;top:48px;font-size:12px}
.f-col h4{font-size:12px;font-weight:700;letter-spacing:.3px;margin-bottom:16px}
.f-col li{list-style:none;line-height:22px;color:#e2e2e2}
.site-footer .socials span{background:var(--white);width:24px;height:24px}
.verified{position:absolute;left:874px;top:125px;width:176px;height:36px;background:#2a2a2a;border-radius:3px;display:flex;align-items:center;gap:10px;font-size:11px}
.verified i{width:40px;height:40px;border-radius:50%;background:var(--orange);display:block;margin-left:-4px}
.f-rule{position:absolute;left:150px;top:212px;width:900px;border-top:1px solid #333}
.copyright{position:absolute;left:0;width:1200px;top:252px;text-align:center;font-size:11px;color:#d8d8d8}
</style>
</head>
<body>

<header class="site-header">
  <div class="brand"><span class="brand__mark"></span>Tail Mart</div>
  <nav class="nav">
    <a class="is-active" style="left:0">Categories</a>
    <a style="left:101px">Popular stores</a>
    <a style="left:235px">Latest deals</a>
    <a style="left:356px">Contact Us</a>
  </nav>
  <div class="socials" aria-label="Social links"><span></span><span></span><span></span><span></span><span></span></div>
</header>

<section class="hero" role="img" aria-label="Happy white poodle puppy running on sunny green grass">
  <h1 class="hero__title">Save on everything<br>your dog loves</h1>
  <div class="search">
    <div class="search__select">Categories <svg width="10" height="6"><path d="M0 0h10L5 6z" fill="#222"/></svg></div>
    <div class="search__input">Search</div>
    <div class="search__btn"><svg width="16" height="16" viewBox="0 0 16 16"><circle cx="7" cy="7" r="5" fill="none" stroke="#fff" stroke-width="2"/><path d="M11 11l4 4" stroke="#fff" stroke-width="2" stroke-linecap="round"/></svg></div>
  </div>
</section>

<div class="deco" role="img" aria-label="Dog chew bone" style="left:-10px;top:430px;width:150px;height:90px;background:#e8d9b4;transform:rotate(28deg);border-radius:40px"></div>
<div class="deco" role="img" aria-label="Basket of colourful dog toys" style="left:1116px;top:438px;width:100px;height:120px;background:#7a5a3a"></div>
<div class="deco" role="img" aria-label="Knotted rope toy" style="left:1122px;top:985px;width:90px;height:110px;background:#e8a23a"></div>
<div class="deco" role="img" aria-label="Red ball toy" style="left:-30px;top:1497px;width:60px;height:70px;background:#d8442c"></div>

<h2 class="section-title" style="top:508px">Our Coupon</h2>

<div class="grid4" style="top:640px">
  <article class="coupon">
    <div class="coupon__media" role="img" aria-label="Bowl of dry dog kibble" style="background:linear-gradient(135deg,#6b3d22,#a0683e 55%,#4a2a18)"><span class="badge-off">25% OFF</span></div>
    <span class="tag">Food</span><div class="store-name">PupPantry</div>
    <p class="desc">Lorem Ipsum is simply dummy text</p>
    <div class="price">$15.00<s>$45.00</s></div>
    <div class="expiry">Expiry Date :&nbsp; 25 June, 2025</div>
    <div class="divider"></div>
    <div class="btn btn--copy">Copy Code : 25de123</div><div class="btn btn--deal">Get Deal</div>
  </article>
  <article class="coupon is-lifted">
    <div class="coupon__media" role="img" aria-label="Terrier running with a rope toy on grass" style="background:linear-gradient(180deg,#8fb06a,#6d9a3c 60%,#4f7d2a)"><span class="badge-off">35% OFF</span></div>
    <span class="tag">Toys</span><div class="store-name">Chewzy</div>
    <p class="desc">Lorem Ipsum is simply dummy text</p>
    <div class="price">$65.00<s>$125.00</s></div>
    <div class="expiry">Expiry Date :&nbsp; 25 June, 2025</div>
    <div class="divider"></div>
    <div class="btn btn--copy btn--copied">Copied Code!</div><div class="btn btn--deal">Get Deal</div>
  </article>
  <article class="coupon">
    <div class="coupon__media" role="img" aria-label="Poodle being groomed" style="background:linear-gradient(135deg,#3c3c44,#9a6b45 55%,#c08a5c)"><span class="badge-off">50% OFF</span></div>
    <span class="tag">Grooming</span><div class="store-name">Groomly</div>
    <p class="desc">Lorem Ipsum is simply dummy text</p>
    <div class="price">$22.00<s>$45.00</s></div>
    <div class="expiry">Expiry Date :&nbsp; 25 June, 2025</div>
    <div class="divider"></div>
    <div class="btn btn--copy">Copy Code : 25de123</div><div class="btn btn--deal">Get Deal</div>
  </article>
  <article class="coupon">
    <div class="coupon__media" role="img" aria-label="Puppy with a tennis ball outdoors" style="background:linear-gradient(180deg,#d6b36a,#a8b25a 50%,#6f9a36)"><span class="badge-off">75% OFF</span></div>
    <span class="tag">Outdoor</span><div class="store-name">TrailPaw</div>
    <p class="desc">Lorem Ipsum is simply dummy text</p>
    <div class="price">$35.00<s>$85.00</s></div>
    <div class="expiry">Expiry Date :&nbsp; 25 June, 2025</div>
    <div class="divider"></div>
    <div class="btn btn--copy">Copy Code : 25de123</div><div class="btn btn--deal">Get Deal</div>
  </article>
</div>

<div class="grid4" style="top:1170px">
  <article class="coupon">
    <div class="coupon__media" role="img" aria-label="Puppy beside a bowl of kibble" style="background:linear-gradient(135deg,#d9cdbd,#b88a5e 60%,#7a4f2c)"><span class="badge-off">25% OFF</span></div>
    <span class="tag">Food</span><div class="store-name">PupPantry</div>
    <p class="desc">Lorem Ipsum is simply dummy text</p>
    <div class="price">$15.00<s>$45.00</s></div>
    <div class="expiry">Expiry Date :&nbsp; 25 June, 2025</div>
    <div class="divider"></div>
    <div class="btn btn--copy">Copy Code : 25de123</div><div class="btn btn--deal">Get Deal</div>
  </article>
  <article class="coupon">
    <div class="coupon__media" role="img" aria-label="Colourful dog toys on pink background" style="background:linear-gradient(135deg,#f2a6b4,#e8879a 50%,#7cc2a8)"><span class="badge-off">35% OFF</span></div>
    <span class="tag">Toys</span><div class="store-name">Chewzy</div>
    <p class="desc">Lorem Ipsum is simply dummy text</p>
    <div class="price">$65.00<s>$125.00</s></div>
    <div class="expiry">Expiry Date :&nbsp; 25 June, 2025</div>
    <div class="divider"></div>
    <div class="btn btn--copy">Copy Code : 25de123</div><div class="btn btn--deal">Get Deal</div>
  </article>
  <article class="coupon">
    <div class="coupon__media" role="img" aria-label="Pug being blow-dried at a groomer" style="background:linear-gradient(135deg,#cfc8bf,#a89883 55%,#4a4440)"><span class="badge-off">50% OFF</span></div>
    <span class="tag">Grooming</span><div class="store-name">Groomly</div>
    <p class="desc">Lorem Ipsum is simply dummy text</p>
    <div class="price">$22.00<s>$45.00</s></div>
    <div class="expiry">Expiry Date :&nbsp; 25 June, 2025</div>
    <div class="divider"></div>
    <div class="btn btn--copy">Copy Code : 25de123</div><div class="btn btn--deal">Get Deal</div>
  </article>
  <article class="coupon">
    <div class="coupon__media" role="img" aria-label="Dog and cat on a meadow" style="background:linear-gradient(180deg,#b9c7a4,#7e9c52 50%,#56782e)"><span class="badge-off">75% OFF</span></div>
    <span class="tag">Outdoor</span><div class="store-name">TrailPaw</div>
    <p class="desc">Lorem Ipsum is simply dummy text</p>
    <div class="price">$35.00<s>$85.00</s></div>
    <div class="expiry">Expiry Date :&nbsp; 25 June, 2025</div>
    <div class="divider"></div>
    <div class="btn btn--copy">Copy Code : 25de123</div><div class="btn btn--deal">Get Deal</div>
  </article>
</div>

<div class="cat-band"></div>
<div class="deco" role="img" aria-label="Dachshund lying down" style="left:38px;top:1718px;width:285px;height:180px;background:#6b4530;border-radius:45% 55% 40% 50%"></div>
<div class="deco" role="img" aria-label="Ginger cat peeking over the edge" style="left:830px;top:1727px;width:240px;height:175px;background:#d88a45;border-radius:50% 50% 20% 20%"></div>
<div class="deco" role="img" aria-label="Striped ball toy" style="left:1168px;top:1838px;width:64px;height:70px;background:#e0a030"></div>

<div class="btn-outline" style="left:523px;top:1744px">View All Deals</div>

<h2 class="section-title" style="top:1914px">Categories</h2>
<a class="cat-card" style="left:152px" role="img" aria-label="Dog food bowl with treats">
  <div style="position:absolute;inset:0;background:linear-gradient(135deg,#4a2e1c,#8a5632 50%,#3a2416)"></div>
  <div class="cat-card__label">Food <svg width="26" height="12"><path d="M0 6h24M18 1l6 5-6 5" fill="none" stroke="#fff" stroke-width="1.6"/></svg></div>
</a>
<a class="cat-card" style="left:455px" role="img" aria-label="Denim bone-shaped chew toys">
  <div style="position:absolute;inset:0;background:linear-gradient(135deg,#cfe4d8,#5d7a9c 50%,#2c4a6e)"></div>
  <div class="cat-card__label">Toys <svg width="26" height="12"><path d="M0 6h24M18 1l6 5-6 5" fill="none" stroke="#fff" stroke-width="1.6"/></svg></div>
</a>
<a class="cat-card" style="left:760px" role="img" aria-label="Beagle and kitten with a first-aid kit">
  <div style="position:absolute;inset:0;background:linear-gradient(135deg,#efe9e4,#c89a6a 45%,#e0356a 80%)"></div>
  <div class="cat-card__label">Health <svg width="26" height="12"><path d="M0 6h24M18 1l6 5-6 5" fill="none" stroke="#fff" stroke-width="1.6"/></svg></div>
</a>
<div class="dots" style="top:2375px"><i class="on"></i><i></i><i></i><i></i></div>

<h2 class="section-title" style="top:2487px">Latest Deals</h2>
<div class="arrow-btn" style="left:60px;top:2835px"><svg width="10" height="16"><path d="M8 1L2 8l6 7" fill="none" stroke="#777" stroke-width="1.6"/></svg></div>
<div class="arrow-btn" style="left:1094px;top:2835px"><svg width="10" height="16"><path d="M2 1l6 7-6 7" fill="none" stroke="#777" stroke-width="1.6"/></svg></div>

<div class="grid4" style="top:2607px">
  <article class="coupon is-lifted" style="height:492px">
    <div class="coupon__media" role="img" aria-label="Red heart-shaped bowl of fresh dog food" style="background:linear-gradient(135deg,#4f7a3a,#c9282a 50%,#8a1a1a)"></div>
    <span class="tag">Food</span><div class="store-name">PupPantry</div>
    <p class="desc">Lorem Ipsum is simply dummy text</p>
    <div class="upto"><span>Upto</span>25% OFF</div>
    <div class="expiry">Expiry Date :&nbsp; 25 June, 2025</div>
    <div class="divider"></div>
    <div class="btn btn--copy">Copied!</div><div class="btn btn--deal">Get Deal</div>
  </article>
  <article class="coupon" style="height:492px">
    <div class="coupon__media" role="img" aria-label="Golden retriever puppy among colourful toys" style="background:linear-gradient(135deg,#c79a5a,#e2b46a 45%,#d84a4a 80%)"></div>
    <span class="tag">Toys &amp; Accessories</span><div class="store-name">PupPantry</div>
    <p class="desc">Lorem Ipsum is simply dummy text</p>
    <div class="upto"><span>Upto</span>35% OFF</div>
    <div class="expiry">Expiry Date :&nbsp; 25 June, 2025</div>
    <div class="divider"></div>
    <div class="btn btn--copy">Copy Code</div><div class="btn btn--deal">Get Deal</div>
  </article>
  <article class="coupon" style="height:492px">
    <div class="coupon__media" role="img" aria-label="Small dog relaxing at a spa" style="background:linear-gradient(135deg,#f1ede8,#d6c4ad 55%,#a8845e)"></div>
    <span class="tag">Health &amp; Grooming</span><div class="store-name">PupPantry</div>
    <p class="desc">Lorem Ipsum is simply dummy text</p>
    <div class="upto"><span>Upto</span>75% OFF</div>
    <div class="expiry">Expiry Date :&nbsp; 25 June, 2025</div>
    <div class="divider"></div>
    <div class="btn btn--copy">Copy Code</div><div class="btn btn--deal">Get Deal</div>
  </article>
  <article class="coupon" style="height:492px">
    <div class="coupon__media" role="img" aria-label="Dachshund in a blue travel backpack" style="background:linear-gradient(135deg,#dedad4,#3b5fa8 50%,#2a2a30)"></div>
    <span class="tag">Outdoor &amp; Travel</span><div class="store-name">PupPantry</div>
    <p class="desc">Lorem Ipsum is simply dummy text</p>
    <div class="upto"><span>Upto</span>50% OFF</div>
    <div class="expiry">Expiry Date :&nbsp; 25 June, 2025</div>
    <div class="divider"></div>
    <div class="btn btn--copy">Copy Code</div><div class="btn btn--deal">Get Deal</div>
  </article>
</div>

<div class="stores-band"></div>
<h2 class="section-title" style="top:3197px">Popular Stores</h2>
<div class="arrow-btn" style="left:60px;top:3388px"><svg width="10" height="16"><path d="M8 1L2 8l6 7" fill="none" stroke="#777" stroke-width="1.6"/></svg></div>
<div class="arrow-btn" style="left:1094px;top:3388px"><svg width="10" height="16"><path d="M2 1l6 7-6 7" fill="none" stroke="#777" stroke-width="1.6"/></svg></div>
<div class="store-grid">
  <div class="store-tile"><i></i>Collar &amp; Co</div>
  <div class="store-tile"><i></i>Lollipaw</div>
  <div class="store-tile"><i></i>Kennel Guard</div>
  <div class="store-tile"><i></i>Wagly</div>
  <div class="store-tile"><i></i>Pawmark</div>
  <div class="store-tile"><i></i>Collar &amp; Co</div>
  <div class="store-tile"><i></i>Lollipaw</div>
  <div class="store-tile"><i></i>Kennel Guard</div>
  <div class="store-tile"><i></i>Wagly</div>
  <div class="store-tile"><i></i>Pawmark</div>
</div>
<div class="deco" role="img" aria-label="Dog holding an orange ball" style="left:35px;top:3488px;width:165px;height:166px;background:#d9b48a;border-radius:50% 50% 0 0"></div>
<div class="btn-outline" style="left:523px;top:3560px">View All Stores</div>

<h2 class="reviews-title">Reviews</h2>
<div class="rating">
  <div class="rating__badge" aria-label="Verified reviews badge"></div>
  <div>
    <div class="stars">
      <svg width="20" height="19" viewBox="0 0 24 23"><path d="M12 0l3.5 7.5 8.2 1-6 5.7 1.6 8.2L12 18.4 4.7 22.4l1.6-8.2-6-5.7 8.2-1z" fill="#f7931e"/></svg>
      <svg width="20" height="19" viewBox="0 0 24 23"><path d="M12 0l3.5 7.5 8.2 1-6 5.7 1.6 8.2L12 18.4 4.7 22.4l1.6-8.2-6-5.7 8.2-1z" fill="#f7931e"/></svg>
      <svg width="20" height="19" viewBox="0 0 24 23"><path d="M12 0l3.5 7.5 8.2 1-6 5.7 1.6 8.2L12 18.4 4.7 22.4l1.6-8.2-6-5.7 8.2-1z" fill="#f7931e"/></svg>
      <svg width="20" height="19" viewBox="0 0 24 23"><path d="M12 0l3.5 7.5 8.2 1-6 5.7 1.6 8.2L12 18.4 4.7 22.4l1.6-8.2-6-5.7 8.2-1z" fill="#f7931e"/></svg>
      <svg width="20" height="19" viewBox="0 0 24 23"><path d="M12 0l3.5 7.5 8.2 1-6 5.7 1.6 8.2L12 18.4 4.7 22.4l1.6-8.2-6-5.7 8.2-1z" fill="#f7931e"/></svg>
    </div>
    <div class="rating__text"><b>4.9</b> Ratings from <b>254</b> Reviews</div>
  </div>
</div>

<article class="review" style="left:150px">
  <div class="review__quote">&ldquo;</div>
  <div class="stars">
    <svg width="16" height="15" viewBox="0 0 24 23"><path d="M12 0l3.5 7.5 8.2 1-6 5.7 1.6 8.2L12 18.4 4.7 22.4l1.6-8.2-6-5.7 8.2-1z" fill="#f7931e"/></svg><svg width="16" height="15" viewBox="0 0 24 23"><path d="M12 0l3.5 7.5 8.2 1-6 5.7 1.6 8.2L12 18.4 4.7 22.4l1.6-8.2-6-5.7 8.2-1z" fill="#f7931e"/></svg><svg width="16" height="15" viewBox="0 0 24 23"><path d="M12 0l3.5 7.5 8.2 1-6 5.7 1.6 8.2L12 18.4 4.7 22.4l1.6-8.2-6-5.7 8.2-1z" fill="#f7931e"/></svg><svg width="16" height="15" viewBox="0 0 24 23"><path d="M12 0l3.5 7.5 8.2 1-6 5.7 1.6 8.2L12 18.4 4.7 22.4l1.6-8.2-6-5.7 8.2-1z" fill="#f7931e"/></svg><svg width="16" height="15" viewBox="0 0 24 23"><path d="M12 0l3.5 7.5 8.2 1-6 5.7 1.6 8.2L12 18.4 4.7 22.4l1.6-8.2-6-5.7 8.2-1z" fill="#f7931e"/></svg>
  </div>
  <p class="review__text">Lorem ipsum dolor sit amet, consec tetur adipiscing elit, sed do eiusmod tempor incididunt ut labore et dolore magna aliqua. Ut enim ad minim veniam quis nostrud exercitation ullamco laboris nisi ut.</p>
  <div class="reviewer"><i role="img" aria-label="Reviewer portrait"></i><div>Jordan Hale<br>2 days Ago</div></div>
</article>
<article class="review" style="left:457px">
  <div class="review__quote">&ldquo;</div>
  <div class="stars">
    <svg width="16" height="15" viewBox="0 0 24 23"><path d="M12 0l3.5 7.5 8.2 1-6 5.7 1.6 8.2L12 18.4 4.7 22.4l1.6-8.2-6-5.7 8.2-1z" fill="#f7931e"/></svg><svg width="16" height="15" viewBox="0 0 24 23"><path d="M12 0l3.5 7.5 8.2 1-6 5.7 1.6 8.2L12 18.4 4.7 22.4l1.6-8.2-6-5.7 8.2-1z" fill="#f7931e"/></svg><svg width="16" height="15" viewBox="0 0 24 23"><path d="M12 0l3.5 7.5 8.2 1-6 5.7 1.6 8.2L12 18.4 4.7 22.4l1.6-8.2-6-5.7 8.2-1z" fill="#f7931e"/></svg><svg width="16" height="15" viewBox="0 0 24 23"><path d="M12 0l3.5 7.5 8.2 1-6 5.7 1.6 8.2L12 18.4 4.7 22.4l1.6-8.2-6-5.7 8.2-1z" fill="#f7931e"/></svg><svg width="16" height="15" viewBox="0 0 24 23"><path d="M12 0l3.5 7.5 8.2 1-6 5.7 1.6 8.2L12 18.4 4.7 22.4l1.6-8.2-6-5.7 8.2-1z" fill="#f7931e"/></svg>
  </div>
  <p class="review__text">Lorem ipsum dolor sit amet, consec tetur adipiscing elit, sed do eiusmod tempor incididunt ut labore et dolore magna aliqua. Ut enim ad minim veniam quis nostrud exercitation ullamco laboris nisi ut.</p>
  <div class="reviewer"><i role="img" aria-label="Reviewer portrait"></i><div>Jordan Hale<br>2 days Ago</div></div>
</article>
<article class="review" style="left:762px">
  <div class="review__quote">&ldquo;</div>
  <div class="stars">
    <svg width="16" height="15" viewBox="0 0 24 23"><path d="M12 0l3.5 7.5 8.2 1-6 5.7 1.6 8.2L12 18.4 4.7 22.4l1.6-8.2-6-5.7 8.2-1z" fill="#f7931e"/></svg><svg width="16" height="15" viewBox="0 0 24 23"><path d="M12 0l3.5 7.5 8.2 1-6 5.7 1.6 8.2L12 18.4 4.7 22.4l1.6-8.2-6-5.7 8.2-1z" fill="#f7931e"/></svg><svg width="16" height="15" viewBox="0 0 24 23"><path d="M12 0l3.5 7.5 8.2 1-6 5.7 1.6 8.2L12 18.4 4.7 22.4l1.6-8.2-6-5.7 8.2-1z" fill="#f7931e"/></svg><svg width="16" height="15" viewBox="0 0 24 23"><path d="M12 0l3.5 7.5 8.2 1-6 5.7 1.6 8.2L12 18.4 4.7 22.4l1.6-8.2-6-5.7 8.2-1z" fill="#f7931e"/></svg><svg width="16" height="15" viewBox="0 0 24 23"><path d="M12 0l3.5 7.5 8.2 1-6 5.7 1.6 8.2L12 18.4 4.7 22.4l1.6-8.2-6-5.7 8.2-1z" fill="#f7931e"/></svg>
  </div>
  <p class="review__text">Lorem ipsum dolor sit amet, consec tetur adipiscing elit, sed do eiusmod tempor incididunt ut labore et dolore magna aliqua. Ut enim ad minim veniam quis nostrud exercitation ullamco laboris nisi ut.</p>
  <div class="reviewer"><i role="img" aria-label="Reviewer portrait"></i><div>Jordan Hale<br>2 days Ago</div></div>
</article>
<div class="dots" style="top:4136px;gap:10px"><i class="on" style="width:9px;height:9px"></i><i style="width:9px;height:9px"></i><i style="width:9px;height:9px"></i><i style="width:9px;height:9px"></i><i style="width:9px;height:9px"></i><i style="width:9px;height:9px"></i></div>
<div class="deco" role="img" aria-label="Puppy lying with colourful chew toys" style="left:980px;top:4011px;width:230px;height:192px;background:#d8a86a;border-radius:50% 40% 0 0"></div>

<footer class="site-footer">
  <div class="brand"><span class="brand__mark"></span>Tail Mart</div>
  <div class="f-col" style="left:412px"><h4>MENU</h4><ul><li>Categories</li><li>Popular stores</li><li>Latest deals</li><li>Contact Us</li></ul></div>
  <div class="f-col" style="left:546px"><h4>CATEGORIES</h4><ul><li>Dog Food &amp; Treats</li><li>Toys &amp; Accessories</li><li>Health &amp; Grooming</li><li>Training &amp; Services</li><li>Outdoor &amp; Travel</li></ul></div>
  <div class="f-col" style="left:725px"><h4>LINKS</h4><ul><li>Terms &amp; Conditions</li><li>FAQ</li><li>Blog</li><li>Privacy</li></ul></div>
  <div class="f-col" style="left:883px"><h4>FOLLOW US</h4></div>
  <div class="socials" style="left:883px;top:80px"><span></span><span></span><span></span><span></span><span></span></div>
  <div class="verified"><i aria-label="Verification badge"></i>100% Deal Verified</div>
  <div class="f-rule"></div>
  <div class="copyright">Copyright © 2025 All Rights Reserved</div>
</footer>

</body>
</html>
```